Facial Tissue Brand Logo and Design

We would like you to design a Logo for the Facial Tissue Brand "Velora" along with the box design. The pack should indicate the pack size (150 x 2 ply). Also our company logo should be present (attached) along with a barcode. The box size dimensions should be 210mm (L) x 110mm (W) x 70mm (H). We are open to all kinds of nice designs which are attractive but not overdone. Happy designing!

UPDATE:
We appreciate the designs so far... but would also love to see more options in a simple and elegent design style that would look good on a table... please see attached below links for reference purpose:

www.pixmarrow.com/image-photo/cleaning-wipes-isolated-on-white-480215736

www.pixmarrow.com/image-photo/cleaning-wipes-isolated-on-white-692048153

www.pixmarrow.com/image-photo/delicate-female-hands-pulling-tissue-out-2875013649

Happy desgining!

We appreciate the designs so far.. but would like to to see some more options.

```html
<!DOCTYPE html>
<html lang="en">
<head>
<meta charset="utf-8">
<title>Velora – Facial Tissue Box Dieline</title>
<link href="https://fonts.googleapis.com/css2?family=Allura&family=Montserrat:wght@400&display=swap" rel="stylesheet">
<style>
  :root {
    --paper: #ffffff;
    --navy: #223159;
    --navy-deep: #0f1c3f;
    --silver: #8c8d99;
    --silver-light: #a4a6b3;
    --cut-line: #1f8fd0;
  }
  * { box-sizing: border-box; margin: 0; padding: 0; }
  html, body { width: 1200px; height: 673px; overflow: hidden; background: var(--paper); }
  .canvas { position: relative; width: 1200px; height: 673px; }

  .dieline { position: absolute; inset: 0; filter: drop-shadow(3px 4px 3px rgba(0,0,0,0.28)); }
  .panel {
    position: absolute;
    background: var(--navy);
    outline: 0.6px solid var(--cut-line);
    overflow: hidden;
  }
  .flap-top-left    { left: 65px;  top: 47px;  width: 83px;  height: 103px; }
  .flap-top-right   { left: 492px; top: 47px;  width: 83px;  height: 103px; }
  .panel-back       { left: 148px; top: 45px;  width: 344px; height: 111px; }
  .panel-end-left   { left: 32px;  top: 156px; width: 116px; height: 173px; }
  .panel-top        { left: 148px; top: 156px; width: 344px; height: 173px; }
  .panel-end-right  { left: 492px; top: 156px; width: 116px; height: 173px; }
  .flap-bot-left    { left: 65px;  top: 334px; width: 83px;  height: 103px; }
  .flap-bot-right   { left: 492px; top: 334px; width: 83px;  height: 103px; }
  .panel-front      { left: 148px; top: 329px; width: 344px; height: 109px; }
  .panel-base       { left: 148px; top: 438px; width: 344px; height: 176px; }
  .glue-strip {
    position: absolute; left: 148px; top: 614px; width: 344px; height: 24px;
    background: var(--paper); border-left: 0.6px solid var(--cut-line);
  }

  .scallop-band { position: absolute; background: var(--navy-deep); }
  .scallop-band::after {
    content: ""; position: absolute; background: var(--silver);
  }
  .band-horizontal { left: 0; width: 100%; height: 24px; }
  .band-horizontal::after { left: 0; right: 0; height: 1px; }
  .panel-back .band-horizontal { top: 0; }
  .panel-back .band-horizontal::after { bottom: 0; }
  .panel-front .band-horizontal { bottom: 0; }
  .panel-front .band-horizontal::after { top: 0; }
  .band-vertical { top: 0; height: 100%; width: 27px; }
  .band-vertical::after { top: 0; bottom: 0; width: 1px; }
  .panel-end-left .band-vertical { left: 0; }
  .panel-end-left .band-vertical::after { right: 0; }
  .panel-end-right .band-vertical { right: 0; }
  .panel-end-right .band-vertical::after { left: 0; }

  .dispenser-opening { position: absolute; left: 80px; top: 51px; }

  .pack-label {
    position: absolute; display: flex; align-items: center; gap: 10px;
    color: var(--silver-light);
  }
  .pack-label .wordmark {
    font-family: "Allura", cursive; font-size: 56px; line-height: 1; color: var(--silver);
  }
  .pack-label .descriptor {
    font-family: "Montserrat", sans-serif; font-size: 9.5px; letter-spacing: 0.4px;
    padding-top: 8px;
  }
  .panel-front .pack-label { left: 22px; top: 20px; }
  .panel-back .pack-label { left: 22px; top: 36px; transform: rotate(180deg); transform-origin: 150px 30px; }

  .company-mark {
    position: absolute; left: 138px; top: 84px; display: flex; align-items: center; gap: 5px;
    font-family: "Montserrat", sans-serif; font-size: 6px; color: var(--cut-line); letter-spacing: 0.3px;
  }
  .company-mark .mark-square { width: 10px; height: 10px; background: var(--cut-line); }

  .brand-logo {
    position: absolute; left: 640px; top: 40px;
    font-family: "Allura", cursive; font-size: 190px; line-height: 1;
    color: var(--silver);
  }
</style>
</head>
<body>
<main class="canvas">
  <section class="dieline" aria-label="Velora tissue box dieline">
    <div class="panel flap-top-left" role="img" aria-label="Navy panel with ginkgo leaf line pattern"></div>
    <div class="panel flap-top-right" role="img" aria-label="Navy panel with ginkgo leaf line pattern"></div>

    <div class="panel panel-back">
      <div class="scallop-band band-horizontal" role="img" aria-label="Silver fan scallop border"></div>
      <div class="pack-label">
        <span class="wordmark">Velora</span>
        <span class="descriptor">2 PLY FACIAL TISSUES</span>
      </div>
    </div>

    <div class="panel panel-end-left">
      <div class="scallop-band band-vertical" role="img" aria-label="Silver fan scallop border"></div>
    </div>

    <div class="panel panel-top" role="img" aria-label="Navy panel with ginkgo leaf line pattern and dispenser opening">
      <svg class="dispenser-opening" width="190" height="74" viewBox="0 0 190 74">
        <ellipse cx="95" cy="37" rx="94" ry="35" fill="none" stroke="var(--cut-line)" stroke-width="0.7"/>
      </svg>
    </div>

    <div class="panel panel-end-right">
      <div class="scallop-band band-vertical" role="img" aria-label="Silver fan scallop border"></div>
    </div>

    <div class="panel flap-bot-left" role="img" aria-label="Navy panel with ginkgo leaf line pattern"></div>
    <div class="panel flap-bot-right" role="img" aria-label="Navy panel with ginkgo leaf line pattern"></div>

    <div class="panel panel-front">
      <div class="pack-label">
        <span class="wordmark">Velora</span>
        <span class="descriptor">2 PLY FACIAL TISSUES</span>
      </div>
      <div class="scallop-band band-horizontal" role="img" aria-label="Silver fan scallop border"></div>
    </div>

    <div class="panel panel-base">
      <div class="company-mark">
        <span class="mark-square"></span>
        <span>NORVIK TRADING</span>
      </div>
    </div>

    <div class="glue-strip"></div>
  </section>

  <h1 class="brand-logo">Velora</h1>
</main>
</body>
</html>
```